Disposable Mini Sauce Pot Design for Asian Chain Food Brands

We operate a Hainan Chicken Rice takeout brand under the name Wokly8, with our official website: www.Wokly8.com.
We offer four signature house sauces and are launching brand-new packaging for our sauce line. We require custom graphic designs exclusively for the sauce cup lids.
Product Material & Base Specs
The sauce cups are made of PP plastic, available in two translucent base options: Translucent White and Translucent Orange.
Four Sauce Varieties for Individual Lid Designs
1. Red Sauce – Fried Sweet Chili Sauce
2.Green Sauce – Scallion Oil Dressing
3.Sweet Soy Sauce
4.Sweet Red Sauce (Special for Fried Chicken)
Differentiate each sauce lid design through unique graphics, typography, or illustrative elements for easy customer identification.
The marking NET WT 2 OZ must be clearly printed on every lid.
**There is no need to print full descriptive text or the full name of the sauces on each lid; the design only needs to clearly differentiate the four sauce varieties.
**Please reference the original design style and brand color palette shown on our official website, and feel free to fully unleash your creativity.
Look and feel
Each slider illustrates characteristics of the customer's brand and the style your logo design should communicate.

```html
<!DOCTYPE html>
<html lang="en">
<head>
<meta charset="utf-8">
<title>Wokly8 Sauce Lids</title>
<link rel="stylesheet" href="https://fonts.googleapis.com/css2?family=Montserrat:wght@700;800;900&display=swap">
<style>
  :root {
    --brand-orange: #ff4a06;
    --white: #ffffff;
    --red-sauce-edge: #f2741c;
    --red-sauce-core: #fbb27c;
    --red-ink: #b5120a;
    --red-shadow: #e0520f;
    --green-sauce-edge: #7fd40a;
    --green-sauce-core: #c9f65a;
    --green-ink: #4caf0e;
    --green-shadow: #3f9a0a;
    --soy-rim: #7a1a12;
    --soy-core: #1c1012;
    --soy-mid: #4a1512;
    --sweet-rim: #e5701e;
    --sweet-core: #c41a06;
    --sweet-mid: #d8300a;
    --dark-shadow: #5a1208;
  }
  * { margin: 0; padding: 0; box-sizing: border-box; }
  html, body { width: 1200px; height: 1000px; overflow: hidden; background: var(--white); }
  body { position: relative; font-family: "Montserrat", Arial, sans-serif; }

  .lid {
    position: absolute;
    width: 287px;
    height: 325px;
    border-radius: 46px;
    overflow: hidden;
  }
  .lid--red { left: 282px; top: 142px; }
  .lid--green { left: 631px; top: 142px; }
  .lid--soy { left: 282px; top: 532px; }
  .lid--sweet { left: 631px; top: 532px; }

  .lid__sauce { position: absolute; inset: 0; }
  .lid--red .lid__sauce { background: radial-gradient(ellipse at 60% 55%, var(--red-sauce-core) 0%, var(--red-sauce-edge) 75%); }
  .lid--green .lid__sauce { background: radial-gradient(ellipse at 55% 55%, var(--green-sauce-core) 0%, var(--green-sauce-edge) 80%); }
  .lid--soy .lid__sauce { background: radial-gradient(ellipse at 50% 55%, var(--soy-core) 0%, var(--soy-core) 45%, var(--soy-mid) 70%, var(--soy-rim) 90%); }
  .lid--sweet .lid__sauce { background: radial-gradient(ellipse at 50% 55%, var(--sweet-core) 0%, var(--sweet-mid) 70%, var(--sweet-rim) 92%); }

  .lid__band { position: absolute; left: 0; top: 0; width: 287px; height: 110px; }
  .lid__band polygon { fill: var(--brand-orange); }

  .lid__brand {
    position: absolute;
    left: 0; right: 0; top: 30px;
    text-align: center;
    font-weight: 900;
    font-size: 50px;
    letter-spacing: -1px;
    color: var(--white);
    line-height: 1;
  }

  .lid__variety, .lid__sauce-word, .lid__weight {
    position: absolute;
    left: 0; right: 0;
    text-align: center;
    line-height: 1;
  }
  .lid__variety { top: 146px; font-size: 33px; font-weight: 800; color: var(--white); }
  .lid__sauce-word { top: 184px; font-size: 60px; font-weight: 900; color: var(--white); letter-spacing: -1px; }
  .lid__weight { top: 279px; font-size: 22px; font-weight: 800; letter-spacing: 0.5px; }

  .lid--red .lid__variety, .lid--red .lid__sauce-word { text-shadow: 2px 3px 0 var(--red-shadow); }
  .lid--red .lid__weight { color: var(--red-ink); }
  .lid--green .lid__variety, .lid--green .lid__sauce-word { text-shadow: 2px 3px 0 var(--green-shadow); }
  .lid--green .lid__weight { color: var(--green-ink); }
  .lid--soy .lid__variety, .lid--soy .lid__sauce-word,
  .lid--sweet .lid__variety, .lid--sweet .lid__sauce-word { text-shadow: 2px 3px 0 var(--dark-shadow); }
  .lid--soy .lid__weight, .lid--sweet .lid__weight { color: var(--white); }

  .lid__gloss { position: absolute; inset: 0; width: 287px; height: 325px; pointer-events: none; }
  .lid__gloss path { fill: none; stroke: var(--white); stroke-width: 3; stroke-linecap: round; }
</style>
</head>
<body>

<section class="lid lid--red">
  <div class="lid__sauce" role="img" aria-label="Orange sweet chili sauce with red chili flakes and garlic bits"></div>
  <svg class="lid__band" viewBox="0 0 287 110"><polygon points="0,0 287,0 287,40 0,98"/></svg>
  <div class="lid__brand">Wokly8</div>
  <div class="lid__variety">RED</div>
  <div class="lid__sauce-word">SAUCE</div>
  <div class="lid__weight">NET WT 2 OZ</div>
  <svg class="lid__gloss" viewBox="0 0 287 325"><path d="M214 313 C245 308 262 300 268 282"/></svg>
</section>

<section class="lid lid--green">
  <div class="lid__sauce" role="img" aria-label="Green scallion oil dressing with chopped scallion pieces"></div>
  <svg class="lid__band" viewBox="0 0 287 110"><polygon points="0,0 287,0 287,40 0,98"/></svg>
  <div class="lid__brand">Wokly8</div>
  <div class="lid__variety">GREEN</div>
  <div class="lid__sauce-word">SAUCE</div>
  <div class="lid__weight">NET WT 2 OZ</div>
  <svg class="lid__gloss" viewBox="0 0 287 325"><path d="M180 312 C235 314 262 300 272 230"/></svg>
</section>

<section class="lid lid--soy">
  <div class="lid__sauce" role="img" aria-label="Dark sweet soy sauce pooled in the cup"></div>
  <svg class="lid__band" viewBox="0 0 287 110"><polygon points="0,0 287,0 287,39 0,97"/></svg>
  <div class="lid__brand">Wokly8</div>
  <div class="lid__variety">SWEET SOY</div>
  <div class="lid__sauce-word">SAUCE</div>
  <div class="lid__weight">NET WT 2 OZ</div>
  <svg class="lid__gloss" viewBox="0 0 287 325"><path d="M176 308 C240 306 266 304 266 254"/></svg>
</section>

<section class="lid lid--sweet">
  <div class="lid__sauce" role="img" aria-label="Sweet red sauce with pink chili seeds"></div>
  <svg class="lid__band" viewBox="0 0 287 110"><polygon points="0,0 287,0 287,39 0,97"/></svg>
  <div class="lid__brand">Wokly8</div>
  <div class="lid__variety">SWEET RED</div>
  <div class="lid__sauce-word">SAUCE</div>
  <div class="lid__weight">NET WT 2 OZ</div>
  <svg class="lid__gloss" viewBox="0 0 287 325"><path d="M36 306 C60 309 90 308 118 306 M196 310 C245 314 268 300 268 254"/></svg>
</section>

</body>
</html>
```